Torquel Australia Pty Ltd

I require professional business cards with our company logo. We would like something that looks sharp and unique. I have attached the logo for our business, which is an industrial electrical contracting company. But this does not need to be shown on the cards.

Industry/Entity Type

Industrial

Requirements
Must have
• The design must be double sided and needs to have one side with our logo only and the other side with our details.
Should not have
• We do not want any lightening bolts on the designs as this is very common.

```html
<!DOCTYPE html>
<html lang="en">
<head>
<meta charset="utf-8">
<title>Torquel Australia Pty Ltd – Business Cards</title>
<link href="https://fonts.googleapis.com/css2?family=Open+Sans:wght@700;800&display=swap" rel="stylesheet">
<style>
  :root {
    --backdrop: #8c7d72;
    --card-black: #111111;
    --card-white: #f1f1ef;
    --gold: #c9a227;
    --gold-deep: #a8831a;
    --gold-light: #f0d35a;
  }
  * { margin: 0; padding: 0; box-sizing: border-box; }
  html, body { width: 1200px; height: 694px; overflow: hidden; }
  body {
    background: var(--backdrop);
    font-family: "Open Sans", Arial, sans-serif;
    position: relative;
  }
  .card {
    position: absolute;
    width: 464px;
    height: 266px;
    overflow: hidden;
  }
  .card--front { left: 77px; top: 220px; background: var(--card-black); }
  .card--back { left: 671px; top: 219px; background: var(--card-white); }

  .wordmark {
    position: absolute;
    display: flex;
    align-items: center;
    gap: 10px;
    color: var(--gold);
    font-weight: 800;
  }
  .wordmark__ring {
    width: 60px; height: 60px;
    border: 4px solid var(--gold);
    border-radius: 50%;
    flex: none;
  }
  .wordmark__name { line-height: 1; }
  .wordmark__name span { display: block; }
  .wordmark__main { font-size: 30px; letter-spacing: 1px; }
  .wordmark__sub { font-size: 11.5px; letter-spacing: 3.2px; margin-top: 4px; }

  .card--front .wordmark { left: 24px; top: 182px; }

  .card--back .wordmark {
    left: 34px; top: 110px;
    flex-direction: column;
    gap: 10px;
    text-align: center;
  }
  .card--back .wordmark__ring { width: 52px; height: 52px; border-width: 3.5px; }
  .card--back .wordmark__main { font-size: 24px; }
  .card--back .wordmark__sub { font-size: 9.5px; letter-spacing: 2.6px; margin-top: 3px; }

  .swoosh { position: absolute; left: 0; top: 0; }

  .contact {
    position: absolute;
    right: 20px;
    top: 60px;
    text-align: right;
    color: var(--gold);
  }
  .contact__name { font-size: 16px; font-weight: 800; letter-spacing: 1.4px; }
  .contact__role { font-size: 11px; font-weight: 800; letter-spacing: 1.2px; margin-top: 4px; }
  .contact__group { margin-top: 22px; }
  .contact__group + .contact__group { margin-top: 16px; }
  .contact__line {
    display: flex;
    justify-content: flex-end;
    align-items: center;
    gap: 8px;
    font-size: 8.5px;
    font-weight: 700;
    line-height: 14px;
  }
  .contact__icon { width: 10px; height: 10px; flex: none; }
  .contact__line--plain { padding-right: 18px; }
</style>
</head>
<body>

  <section class="card card--front" aria-label="Business card front">
    <div class="wordmark">
      <div class="wordmark__ring"></div>
      <div class="wordmark__name">
        <span class="wordmark__main">TORQUEL</span>
        <span class="wordmark__sub">AUSTRALIA PTY LTD</span>
      </div>
    </div>
  </section>

  <section class="card card--back" aria-label="Business card back">
    <svg class="swoosh" width="464" height="266" viewBox="0 0 464 266" aria-hidden="true">
      <path d="M138,0 L190,0 Q300,135 196,266 L184,266 Q262,130 138,0 Z" fill="var(--gold)"/>
      <path d="M4,126 Q100,40 212,112 Q100,58 4,126 Z" fill="var(--gold)"/>
    </svg>

    <div class="wordmark">
      <div class="wordmark__ring"></div>
      <div class="wordmark__name">
        <span class="wordmark__main">TORQUEL</span>
        <span class="wordmark__sub">AUSTRALIA PTY LTD</span>
      </div>
    </div>

    <div class="contact">
      <div class="contact__name">REID HALSTON</div>
      <div class="contact__role">DIRECTOR</div>

      <div class="contact__group">
        <div class="contact__line">PO BOX 318
          <svg class="contact__icon" viewBox="0 0 10 10" aria-hidden="true"><path d="M5,0.5 A3.4,3.4 0 0 1 8.4,3.9 C8.4,6.3 5,9.5 5,9.5 C5,9.5 1.6,6.3 1.6,3.9 A3.4,3.4 0 0 1 5,0.5 Z M5,2.6 A1.3,1.3 0 1 0 5,5.2 A1.3,1.3 0 1 0 5,2.6 Z" fill="var(--gold)" fill-rule="evenodd"/></svg>
        </div>
        <div class="contact__line contact__line--plain">CARRICK NSW 2571</div>
      </div>

      <div class="contact__group">
        <div class="contact__line">02 4719 5832
          <svg class="contact__icon" viewBox="0 0 10 10" aria-hidden="true"><path d="M1,3 Q5,0.5 9,3 L8,4.6 L6.6,4 L6.6,3.2 Q5,2.6 3.4,3.2 L3.4,4 L2,4.6 Z M2.4,5.4 L7.6,5.4 L8.6,9 L1.4,9 Z" fill="var(--gold)"/></svg>
        </div>
        <div class="contact__line">0431 276 905
          <svg class="contact__icon" viewBox="0 0 10 10" aria-hidden="true"><rect x="2.4" y="0.5" width="5.2" height="9" rx="0.9" fill="none" stroke="var(--gold)" stroke-width="1.1"/><rect x="4.2" y="7.6" width="1.6" height="0.9" fill="var(--gold)"/></svg>
        </div>
      </div>

      <div class="contact__group">
        <div class="contact__line">REID@TORQUELAUSTRALIA.COM.AU
          <svg class="contact__icon" viewBox="0 0 10 10" aria-hidden="true"><rect x="0.8" y="2" width="8.4" height="6" fill="none" stroke="var(--gold)" stroke-width="1.1"/><path d="M0.8,2 L5,5.4 L9.2,2" fill="none" stroke="var(--gold)" stroke-width="1.1"/></svg>
        </div>
        <div class="contact__line">WWW.TORQUELAUSTRALIA.COM.AU
          <svg class="contact__icon" viewBox="0 0 10 10" aria-hidden="true"><circle cx="5" cy="5" r="4.2" fill="none" stroke="var(--gold)" stroke-width="1.1"/><ellipse cx="5" cy="5" rx="1.8" ry="4.2" fill="none" stroke="var(--gold)" stroke-width="0.9"/><line x1="0.8" y1="5" x2="9.2" y2="5" stroke="var(--gold)" stroke-width="0.9"/></svg>
        </div>
      </div>
    </div>
  </section>

</body>
</html>
```